House Builder and Property Development Card Design and Logo

I need a business card design for a building and property development company.
Colour scheme of Dark Grey and Green, I would like it bold, sharp and professional.
No logo yet done, I'm open to options but please stay away from the usual- house, roof, hammers etc.
Thanks Lou
Updates

Please be aware that on the business card information section the VKRT # 5382917 is a licence number and my phone number 0461739258. The numbers are close together and could be mistaken as one whole number 

Thank you

                                   

Industry/Entity Type

Building

Contact Information for Business Card

HARLOW BUILD & DEVELOPMENT.
Residential Building & Property Development
Louis Harlow - Director
VKRT # 5382917
0461739258
lou@harlowbuild.com.au

Requirements
Must have
• Bold Business name
Dark grey and green colours
Should not have
• roof outline or hammer logo

```html
<!DOCTYPE html>
<html lang="en">
<head>
<meta charset="utf-8">
<title>Harlow Build &amp; Development – Business Card</title>
<link rel="stylesheet" href="https://fonts.googleapis.com/css2?family=Gelasio:wght@400;700&family=Arimo:ital,wght@1,700&display=swap">
<style>
  :root {
    --page-bg: #e4e4e4;
    --card-dark: #15181a;
    --card-mid: #2a2c2e;
    --brand-green: #4fa83a;
    --brand-green-light: #8cc83f;
    --text-light: #f2f2f2;
    --divider-dark: #0e1011;
  }
  * { margin: 0; padding: 0; box-sizing: border-box; }
  html, body { width: 1200px; height: 1000px; overflow: hidden; }
  body {
    position: relative;
    background: var(--page-bg);
    font-family: "Gelasio", Georgia, serif;
  }
  .card {
    position: absolute;
    width: 705px;
    height: 403px;
    border-radius: 42px 0 42px 0;
    background: radial-gradient(ellipse at 55% 45%, var(--card-mid) 0%, var(--card-dark) 75%);
    overflow: hidden;
  }
  .card--front { left: 117px; top: 60px; }
  .card--back { left: 380px; top: 521px; }

  /* Front */
  .brand-lockup {
    position: absolute;
    left: 143px;
    top: 124px;
    display: flex;
    align-items: flex-start;
    gap: 16px;
  }
  .brand-square {
    width: 58px;
    height: 58px;
    background: var(--brand-green);
    margin-top: 8px;
  }
  .brand-name {
    color: var(--brand-green);
    font-size: 36px;
    line-height: 44px;
    font-weight: 400;
    letter-spacing: 0.3px;
  }
  .brand-tagline {
    position: absolute;
    left: 217px;
    top: 244px;
    color: var(--text-light);
    font-size: 13.5px;
    font-weight: 700;
  }

  /* Back */
  .back-mark {
    position: absolute;
    left: 86px;
    top: 96px;
    width: 150px;
    display: flex;
    flex-direction: column;
    align-items: center;
    gap: 14px;
  }
  .back-mark .brand-square { width: 84px; height: 84px; margin: 0; }
  .back-mark__name {
    color: var(--brand-green);
    font-size: 28px;
    line-height: 32px;
    text-align: center;
  }
  .card-divider {
    position: absolute;
    left: 320px;
    top: 55px;
    width: 2px;
    height: 270px;
    background: linear-gradient(to bottom, transparent, var(--divider-dark) 30%, var(--divider-dark) 70%, transparent);
    box-shadow: 3px 0 8px rgba(0,0,0,0.5);
  }
  .contact {
    position: absolute;
    left: 356px;
    top: 124px;
    color: var(--text-light);
  }
  .contact__name { font-size: 27px; line-height: 34px; }
  .contact__role { font-size: 18px; line-height: 26px; margin-top: 2px; }
  .contact__list { list-style: none; margin-top: 26px; font-size: 17.5px; }
  .contact__item { display: flex; align-items: center; height: 30px; gap: 6px; }
  .contact__icon { width: 20px; height: 18px; flex: none; }
  .licence {
    position: absolute;
    right: 42px;
    bottom: 22px;
    color: var(--text-light);
    font-family: "Arimo", Arial, sans-serif;
    font-style: italic;
    font-weight: 700;
    font-size: 16px;
  }
</style>
</head>
<body>

<section class="card card--front" aria-label="Card front">
  <div class="brand-lockup">
    <div class="brand-square"></div>
    <div class="brand-name">HARLOW BUILD<br>&amp; DEVELOPMENT</div>
  </div>
  <p class="brand-tagline">Residential Building &amp; Property Development</p>
</section>

<section class="card card--back" aria-label="Card back">
  <div class="back-mark">
    <div class="brand-square"></div>
    <div class="back-mark__name">HARLOW<br>BUILD</div>
  </div>
  <div class="card-divider"></div>
  <div class="contact">
    <p class="contact__name">Louis Harlow</p>
    <p class="contact__role">(Director)</p>
    <ul class="contact__list">
      <li class="contact__item">
        <svg class="contact__icon" viewBox="0 0 20 18" aria-hidden="true">
          <rect x="5" y="1" width="9" height="16" rx="1.5" fill="none" stroke="#f2f2f2" stroke-width="1.6"/>
          <rect x="7" y="3.5" width="5" height="5" fill="#f2f2f2"/>
        </svg>
        <span>: 046.173.9258</span>
      </li>
      <li class="contact__item">
        <svg class="contact__icon" viewBox="0 0 20 18" aria-hidden="true">
          <rect x="1" y="3" width="18" height="12" fill="#f2f2f2"/>
          <path d="M1 3 L10 10 L19 3" fill="none" stroke="#15181a" stroke-width="1.4"/>
        </svg>
        <span>: lou@harlowbuild.com.au</span>
      </li>
    </ul>
  </div>
  <p class="licence">VKRT # 5382917</p>
</section>

</body>
</html>
```